Seeking funky, innovative business cards

I am looking to refresh our current business cards to something more engaging, visual and impactful. We are a management consultancy firm, see website (www.thornbury-partners.com.au). I've included our colour scheme, sample of the slides we use and our old business cards. We would like our cards to have icons. The card should display:- Name- Title- Mobile number- Address- Email address- Website - Company logo- Our purpose statement "we shape the brightest teams in every workplace"

Contact Information for Business Card

Radek Solvieri
Consultant
0491 627 358
Level 3, 218 Wexford Street, Melbourne 3000
radek@thornbury-partners.com.au
www.thornbury-partners.com.au

Purpose statement "we shape the brightest teams in every workplace"
LOGO available in google images

Font styles to use
Other font styles liked:
• Open Sans Light, Bebas Neue (open to other cool foints)

Colors
ffc214
5c5c5c
f5f5f5
fefefe

Requirements
Must have
• - Name
• - Title
• - Mobile number
• - Address
• - Email address
• - Website
• - Company logo
• - Our purpose statement "we shape the brightest teams in every workplace"
Nice to have
• - Icons
• - Colour (see our colour scheme"

```html
<!DOCTYPE html>
<html lang="en">
<head>
<meta charset="utf-8">
<title>Thornbury Partners – Business Card</title>
<link rel="stylesheet" href="https://fonts.googleapis.com/css2?family=Roboto:ital,wght@0,400;0,500;1,400;1,500&display=swap">
<style>
  :root {
    --backdrop: #b9b9b9;
    --card-white: #fefefe;
    --card-grey: #d1d4d7;
    --accent: #f9a825;
    --accent-gold: #ffc214;
    --ink: #3f3f3f;
    --ink-soft: #5c5c5c;
    --white: #ffffff;
  }
  * { margin: 0; padding: 0; box-sizing: border-box; }
  html, body {
    width: 1200px; height: 1200px; overflow: hidden;
    background: var(--backdrop);
    font-family: "Roboto", Arial, sans-serif;
  }
  .card {
    position: absolute; left: 217px; width: 800px; height: 457px; overflow: hidden;
  }
  .card--front { top: 115px; background: var(--card-white); }
  .card--back { top: 638px; background: var(--card-grey); }

  .brand {
    position: absolute; right: 55px; top: 98px;
    display: flex; align-items: center; gap: 12px;
    color: var(--ink-soft); font-weight: 400; font-size: 40px; letter-spacing: -0.5px;
  }
  .brand__dot { width: 14px; height: 14px; border-radius: 50%; background: var(--accent); }

  .contact { position: absolute; left: 60px; top: 278px; color: var(--ink-soft); }
  .contact__name { color: var(--accent); font-size: 29px; font-weight: 500; line-height: 1.1; }
  .contact__title { color: var(--ink); font-size: 20px; font-weight: 500; margin-top: 3px; }
  .contact__address { font-size: 19.5px; margin-top: 7px; }
  .contact__lines { font-size: 19.5px; margin-top: 6px; }
  .contact__label { color: var(--accent); font-weight: 500; }

  .band { position: absolute; left: 0; bottom: 0; width: 100%; height: 41px; background: var(--card-grey); }
  .band__fill {
    position: absolute; left: 0; top: 0; height: 100%; width: 660px;
    background: var(--accent);
    clip-path: polygon(0 0, 100% 0, 96% 100%, 0 100%);
  }
  .band__web {
    position: absolute; left: 61px; top: 9px;
    color: var(--white); font-size: 18px; font-weight: 500; letter-spacing: 2.2px;
  }
  .band__dot {
    position: absolute; left: 680px; top: 15px; width: 11px; height: 11px;
    border-radius: 50%; background: var(--accent);
  }

  .back-brand {
    position: absolute; left: 0; right: 0; top: 180px;
    display: flex; justify-content: center; align-items: center; gap: 20px;
    color: var(--white); font-size: 60px; font-weight: 400; letter-spacing: -0.5px;
  }
  .back-brand__dot { width: 30px; height: 30px; border-radius: 50%; background: var(--accent-gold); }
  .tagline {
    position: absolute; left: 0; right: 0; top: 381px; text-align: center;
    font-size: 21px; font-style: italic; font-weight: 500; color: var(--white);
  }
  .tagline__accent { color: var(--accent); }
</style>
</head>
<body>
  <section class="card card--front">
    <div class="brand"><span class="brand__name">Thornbury Partners</span><span class="brand__dot"></span></div>
    <div class="contact">
      <p class="contact__name">Radek Solvieri</p>
      <p class="contact__title">Consultant</p>
      <p class="contact__address">Level 3, 218 Wexford Street, Melbourne 3000</p>
      <p class="contact__lines"><span class="contact__label">P:</span> 0491 627 358 <span class="contact__label">E:</span> radek@thornbury-partners.com.au</p>
    </div>
    <div class="band">
      <div class="band__fill"></div>
      <span class="band__web">www.thornbury-partners.com.au</span>
      <span class="band__dot"></span>
    </div>
  </section>

  <section class="card card--back">
    <div class="back-brand"><span class="back-brand__dot"></span><span>Thornbury Partners</span></div>
    <p class="tagline">we shape the brightest teams <span class="tagline__accent">in every workplace</span></p>
  </section>
</body>
</html>
```